New Zealand Luggage Importer Needs Business Cards

We need professional, creative and fashionable business cards created.
We are based in New Zealand and import and distribute high-end, quality, fashionable and durable luggage.
We pride ourselves on selling the very best quality luggage, second only to 1 brand (which we won't mention here)...we use the same manufacturer. However, our prices are much more reasonable.
Industry/Entity Type
Business
Contact Information for Business Card
Mark Dunsley
027 512 4068
3/17 Harlow Street, Pinecrest Flats, Auckland, 0614
PO Box 204377, Fernside, Auckland 0731
09-528-3916
sales@brivancases.co.nz / www.brivancases.co.nz

```html
<!DOCTYPE html>
<html lang="en">
<head>
<meta charset="utf-8">
<title>Brivan Cases – Business Card</title>
<link rel="stylesheet" href="https://fonts.googleapis.com/css2?family=Exo+2:wght@400;500;700;800&display=swap">
<style>
  :root {
    --backdrop: #2a2a2a;
    --ink: #221e1f;
    --paper: #ffffff;
    --gold: #d9b44a;
    --yellow: #e6c65c;
    --stripe: #ebebeb;
    --stripe-line: #d6d6d6;
  }
  * { box-sizing: border-box; margin: 0; padding: 0; }
  html, body { width: 1200px; height: 1000px; overflow: hidden; }
  body {
    background: var(--backdrop);
    font-family: "Exo 2", sans-serif;
    position: relative;
  }
  .card {
    position: absolute;
    width: 665px;
    height: 380px;
    overflow: hidden;
    box-shadow: 0 12px 30px rgba(0,0,0,.45);
  }
  /* back side */
  .card--back {
    left: 420px; top: 60px;
    background: var(--ink);
    display: flex; align-items: center; justify-content: center;
  }
  .card--back .brand-name { color: var(--paper); }
  .brand-name {
    font-family: "Exo 2", sans-serif;
    font-weight: 800;
    font-size: 60px;
    letter-spacing: 1px;
    line-height: 1;
    white-space: nowrap;
  }
  /* front side */
  .card--front {
    left: 115px; top: 520px;
    background: var(--paper);
  }
  .card--front .brand-name {
    position: absolute; left: 70px; top: 38px;
    color: var(--ink);
  }
  .address {
    position: absolute; left: 250px; top: 122px;
    font-size: 14px; font-weight: 500; line-height: 1.5;
    color: var(--ink);
  }
  .band-shapes { position: absolute; left: 0; top: 0; }
  .holder-name {
    position: absolute; left: 0; top: 250px; width: 390px;
    text-align: center;
    font-weight: 700; font-size: 36px; letter-spacing: 1px;
    color: var(--gold);
  }
  .contact-list {
    position: absolute; left: 425px; top: 252px;
    list-style: none;
    font-size: 14px; font-weight: 500; color: var(--ink);
  }
  .contact-list li {
    display: flex; align-items: center; gap: 12px;
    height: 20px;
  }
  .contact-list svg { width: 14px; height: 14px; flex: none; }
  .foot-stripe {
    position: absolute; left: 0; bottom: 0; width: 100%; height: 42px;
    background: var(--stripe);
    border-top: 6px solid var(--paper);
  }
</style>
</head>
<body>

<section class="card card--back" aria-label="Card back">
  <div class="brand-name">BRIVAN CASES</div>
</section>

<section class="card card--front" aria-label="Card front">
  <div class="brand-name">BRIVAN CASES</div>

  <p class="address">
    3/17 Harlow Street, Pinecrest Flats, Auckland, 0614<br>
    PO Box 204377, Fernside, Auckland 0731
  </p>

  <svg class="band-shapes" width="665" height="380" viewBox="0 0 665 380" aria-hidden="true">
    <rect x="370" y="240" width="295" height="98" fill="var(--yellow)"/>
    <polygon fill="var(--ink)"
      points="0,200 215,200 227,186 239,200 390,200 390,288 404,300 390,312 390,338 0,338"/>
  </svg>

  <div class="holder-name">MARK DUNSLEY</div>

  <ul class="contact-list">
    <li>
      <svg viewBox="0 0 16 16"><path fill="var(--ink)" d="M1 5c0-2 3-3 7-3s7 1 7 3v1h-3V4.5H4V6H1z M3 7h10l1 7H2z"/><circle cx="8" cy="10.5" r="1.8" fill="var(--yellow)"/></svg>
      027 512 4068
    </li>
    <li>
      <svg viewBox="0 0 16 16"><path fill="var(--ink)" d="M3 1l3 3-1.5 2c1 2 3 4 5 5L11.5 9.5l3 3L12 15C6 14 2 10 1 4z"/></svg>
      09-528-3916
    </li>
    <li>
      <svg viewBox="0 0 16 16"><rect x="1" y="3" width="14" height="10" fill="var(--ink)"/><path d="M1 3l7 6 7-6" fill="none" stroke="var(--yellow)" stroke-width="1.2"/></svg>
      sales@brivancases.co.nz
    </li>
    <li>
      <svg viewBox="0 0 16 16"><circle cx="8" cy="8" r="7" fill="var(--ink)"/><path d="M1 8h14M8 1v14M3 4h10M3 12h10" stroke="var(--yellow)" stroke-width="0.9" fill="none"/><ellipse cx="8" cy="8" rx="3" ry="7" fill="none" stroke="var(--yellow)" stroke-width="0.9"/></svg>
      www.brivancases.co.nz
    </li>
  </ul>

  <div class="foot-stripe" role="img" aria-label="Light grey band with fine diagonal line pattern"></div>
</section>

</body>
</html>
```